WeatheredIt.net wordpress design

Concept: Website where personal stories, personal videos can be posted as a challenge while awaiting the wisdom of experience from others who have survived this same event or challenge in their lifetime.
Support aspects will be in 4 quadrants of Challenges:
1. Financial 2. Medical & Physical
3. Legal Matters 4. Psychological & Spiritual - ability to chat online with a spiritual/psychological counselor or life coach
Updates
Wanted to thank all of you for your designs! Greatly appreciated. Very creative ideas that captured the essence of this website. Will be back with a selection very shortly.
Target Market(s)
Anyone looking for a solution based upon experiential wisdom
Industry/Entity Type
Financial
Requirements
Must have
- Interactive website: Where you can post a challenge or issue via a written question or a video and ask for a solution.
Ability to access any of the 4 Quadrants (as listed above) to ask for an expert, via experience, advice and wisdom from those who have similar challenges.

```html
<!DOCTYPE html>
<html lang="en">
<head>
<meta charset="utf-8">
<title>WeatheredIt.net</title>
<link href="https://fonts.googleapis.com/css2?family=PT+Sans+Narrow:wght@400;700&family=PT+Sans:ital,wght@0,400;1,400&family=Dancing+Script:wght@500&display=swap" rel="stylesheet">
<style>
:root{
  --blue:#4a82a2;
  --blue-soft:#6799b3;
  --blue-text:#4f87a3;
  --yellow:#f8d84a;
  --yellow-deep:#f3c41e;
  --grey-field:#f1f1f1;
  --ink:#3d3d3d;
  --footer:#5a5a5a;
  --footer-bg:#e6e6e6;
  --white:#ffffff;
}
*{box-sizing:border-box;margin:0;padding:0}
html,body{width:1200px;height:1097px;overflow:hidden;background:var(--white)}
body{position:relative;font-family:"PT Sans Narrow",sans-serif;color:var(--ink)}
.band{position:absolute;left:0;top:93px;width:1200px;height:314px;background:var(--blue)}
.page{position:absolute;left:136px;top:26px;width:926px;height:1026px;background:var(--white);box-shadow:0 0 14px rgba(0,0,0,.18)}
.header{position:absolute;left:136px;top:0;width:926px;height:80px;background:var(--white)}
.brand{position:absolute;left:35px;top:20px;display:flex;align-items:center;gap:8px;font-size:26px;font-weight:700;color:var(--yellow-deep);letter-spacing:.5px}
.brand-mark{width:28px;height:28px;background:var(--yellow-deep)}
.nav{position:absolute;right:0;top:34px;display:flex;gap:38px;list-style:none}
.nav li{font-size:14px;letter-spacing:1.5px;color:var(--blue-text)}
.hero{position:absolute;left:136px;top:80px;width:926px;height:314px;background:linear-gradient(180deg,#82acc6 0%,#6e9ebb 45%,#6799b3 100%)}
.tagline{position:absolute;left:44px;top:20px;width:840px;font-family:"Dancing Script",cursive;font-weight:500;font-size:27px;color:var(--white);white-space:nowrap;overflow:hidden}
.tagline em{font-style:normal;color:var(--yellow)}
.quadrant{position:absolute;top:82px;width:206px;height:206px;background:#ececec;padding:8px}
.quadrant .photo{width:190px;height:190px;position:relative}
.quadrant .label{position:absolute;left:0;bottom:0;width:100%;height:31px;background:rgba(40,40,40,.75);color:var(--white);font-size:17px;letter-spacing:1px;text-align:center;line-height:33px}
.strip{position:absolute;left:136px;top:394px;width:926px;height:80px;background:linear-gradient(180deg,#ececec,#dedede);border-top:1px solid #d4d4d4;border-bottom:1px solid #d4d4d4}
.strip p{position:absolute;left:35px;top:22px;font-size:26px;letter-spacing:1.3px;color:var(--ink);white-space:nowrap}
.search-btn{position:absolute;left:691px;top:16px;width:198px;height:45px;background:linear-gradient(180deg,var(--yellow),var(--yellow-deep));border:3px solid var(--white);box-shadow:0 0 3px rgba(0,0,0,.2);color:var(--white);font-weight:700;font-size:21px;letter-spacing:.5px;text-align:center;line-height:39px;text-shadow:0 1px 1px rgba(0,0,0,.3)}
.intro{position:absolute;left:171px;top:497px;width:600px;font-size:11.5px;line-height:21px;letter-spacing:.6px;color:var(--ink)}
.form{position:absolute;top:561px;width:397px}
.form-head{height:41px;padding-left:14px;font-family:"Dancing Script",cursive;font-weight:500;font-size:26px;color:var(--white);line-height:41px}
.form-body{position:relative;height:399px;border:1px solid #dcdcdc;border-top:none;background:var(--white)}
.ask .form-head{background:var(--yellow)}
.video .form-head{background:var(--blue-soft)}
.field-label{position:absolute;left:14px;font-size:14px;letter-spacing:1px;color:var(--blue-text)}
.field{position:absolute;left:14px;width:366px;height:37px;background:var(--grey-field);border-radius:2px;font-family:"PT Sans",sans-serif;font-style:italic;font-size:10.5px;letter-spacing:1px;color:#8a8a8a;padding:0 11px;line-height:37px;white-space:nowrap}
.field.area{height:86px;line-height:20px;padding-top:7px}
.select-arrow{position:absolute;right:0;top:0;width:36px;height:37px;border-radius:0 2px 2px 0}
.ask .select-arrow{background:var(--yellow-deep)}
.video .select-arrow{background:var(--blue-soft)}
.browse{position:absolute;left:308px;width:72px;height:37px;border:1px solid #d6d6d6;background:#f6f6f6;font-size:14px;letter-spacing:1px;color:var(--blue-text);text-align:center;line-height:35px;border-radius:2px}
.submit{position:absolute;right:16px;top:357px;width:72px;height:31px;color:var(--white);font-weight:700;font-size:17px;text-align:center;line-height:31px;text-shadow:0 1px 1px rgba(0,0,0,.3)}
.ask .submit{background:var(--yellow-deep)}
.video .submit{background:var(--blue-soft)}
.footer-band{position:absolute;left:0;top:1052px;width:1200px;height:45px;background:var(--footer-bg)}
.footer{position:absolute;left:136px;top:1052px;width:926px;height:45px;background:var(--footer);color:var(--white);font-size:10.5px;letter-spacing:.8px;line-height:45px}
.footer .copy{position:absolute;left:35px}
.footer .copy span{color:#8fc0dc}
.footer ul{position:absolute;right:35px;top:0;display:flex;gap:16px;list-style:none}
.footer li.active{color:#8fc0dc}
</style>
</head>
<body>
<div class="band"></div>
<div class="page"></div>

<header class="header">
  <div class="brand"><span class="brand-mark"></span>WeatheredIt.net</div>
  <ul class="nav"><li>HOME</li><li>ABOUT</li><li>JOIN</li><li>ASK</li><li>BLOG</li><li>CONTACT</li></ul>
</header>

<section class="hero">
  <h1 class="tagline">Tackle Your problems with the <em>wisdom &amp; experience from those who have survived</em></h1>
  <div class="quadrant" style="left:35px"><div class="photo" role="img" aria-label="Businessman on a ladder against a cloudy sky" style="background:linear-gradient(180deg,#8d979e,#b3b8b8 55%,#7c8384)"><span class="label">Financial</span></div></div>
  <div class="quadrant" style="left:253px"><div class="photo" role="img" aria-label="Doctor holding a folder in a hospital corridor" style="background:linear-gradient(135deg,#e7d9a2,#c9b27a 50%,#eadfbf)"><span class="label">Medical &amp; Physical</span></div></div>
  <div class="quadrant" style="left:471px"><div class="photo" role="img" aria-label="Lawyer reading a book at a desk" style="background:linear-gradient(135deg,#3b2418,#8a4a22 50%,#c9a57c)"><span class="label">Legal Matters</span></div></div>
  <div class="quadrant" style="left:688px"><div class="photo" role="img" aria-label="Stepping stones across calm water at sunset" style="background:linear-gradient(180deg,#a99a86,#c8b08c 40%,#3e3a36)"><span class="label">Psychological</span></div></div>
</section>

<section class="strip">
  <p>Lorem ipsum dolor sit amet, consectetur adipiscing elititre ont</p>
  <div class="search-btn">SEARCH QUESTIONS</div>
</section>

<p class="intro">Praesent vulputate lacinia neque vel fermentum. Donec euismod, lorem sit amet bibendum volutpat, sapien quam tincidunt neque, ut dapibus justo metus sit amet justo. Aliquam erat volutpat. Suspendisse non dolor in nisi blandit adipiscing sit</p>

<section class="form ask" style="left:171px">
  <h2 class="form-head">Ask your Question</h2>
  <div class="form-body">
    <span class="field-label" style="top:15px">Your Name</span>
    <div class="field" style="top:42px">Please enter full name...</div>
    <span class="field-label" style="top:87px">Your Email</span>
    <div class="field" style="top:114px">Please enter email address...</div>
    <span class="field-label" style="top:160px">Select the challenge quadrant</span>
    <div class="field" style="top:186px">1.&nbsp; Financial
      <span class="select-arrow"><svg width="36" height="37" viewBox="0 0 36 37"><path d="M12 15h12l-6 9z" fill="#fff"/></svg></span></div>
    <span class="field-label" style="top:235px">Your Question</span>
    <div class="field area" style="top:260px">Find the solution to whatever your challenge or problem is...</div>
    <div class="submit">SUBMIT</div>
  </div>
</section>

<section class="form video" style="left:632px">
  <h2 class="form-head">Post a Video</h2>
  <div class="form-body">
    <span class="field-label" style="top:15px">Your Name</span>
    <div class="field" style="top:42px">Please enter full name...</div>
    <span class="field-label" style="top:87px">Your Email</span>
    <div class="field" style="top:114px">Please enter email address...</div>
    <span class="field-label" style="top:160px">Select the challenge quadrant</span>
    <div class="field" style="top:186px">1.&nbsp; Financial
      <span class="select-arrow"><svg width="36" height="37" viewBox="0 0 36 37"><path d="M12 15h12l-6 9z" fill="#fff"/></svg></span></div>
    <span class="field-label" style="top:235px">Upload your video</span>
    <div class="field" style="top:263px;width:288px">Browse your computer</div>
    <div class="browse" style="top:263px">Browse</div>
    <div class="field" style="top:309px">Or entre cliptube, reelhub, etc URL link</div>
    <div class="submit">SUBMIT</div>
  </div>
</section>

<div class="footer-band"></div>
<footer class="footer">
  <p class="copy">Copyright © 2012 <span>Northfield Studio</span> All rights reserved</p>
  <ul><li class="active">Home</li><li>About</li><li>Join</li><li>Ask</li><li>Blog</li><li>Contact</li></ul>
</footer>
</body>
</html>
```